Valto Sàrl - Business Card

VALTO Sàrl operates in the sector Services for banks and credit institutions. It is a B2B which connects companies. The main colors should be Blue and Black. The logo and look of the card should be simple, professional, conservative and reflect Connecting People.

Target Market(s)

Financial professionals and institutions

Industry/Entity Type

Finance

Contact Information for Business Card

Chemin des Prés 9
1027 Lonay

Logo Text

VALTO Sàrl

Font styles to use
Serif
Sans Serif

Colors
0355a3
3176b5
85acd3
cfdeed

Requirements
Should not have
• Multiple colors

```html
<!DOCTYPE html>
<html lang="fr">
<head>
<meta charset="utf-8">
<title>Valto Sàrl – Business Card</title>
<link rel="stylesheet" href="https://fonts.googleapis.com/css2?family=Montserrat:wght@400;500;600&display=swap">
<style>
  :root {
    --stage: #1b1b1c;
    --card: #262627;
    --card-edge: #2f2f30;
    --blue: #1a7fd0;
    --white: #f2f2f2;
    --silver: #b9b9bb;
  }
  * { box-sizing: border-box; margin: 0; padding: 0; }
  html, body { width: 1200px; height: 900px; overflow: hidden; }
  body {
    background: var(--stage);
    font-family: "Montserrat", sans-serif;
    color: var(--white);
    position: relative;
  }
  .card {
    position: absolute;
    left: 290px;
    width: 620px;
    height: 354px;
    background: linear-gradient(135deg, var(--card-edge), var(--card));
    border-radius: 2px;
  }
  .card--front { top: 58px; }
  .card--back { top: 472px; }

  /* front */
  .front-mark {
    position: absolute;
    inset: 0;
    display: flex;
    align-items: center;
    justify-content: center;
    gap: 14px;
  }
  .front-mark .dot {
    width: 34px; height: 34px; border-radius: 50%;
    background: var(--silver);
  }
  .front-mark .name {
    font-size: 34px; font-weight: 600; letter-spacing: 2px;
    color: var(--silver);
  }

  /* back */
  .brand {
    position: absolute;
    left: 40px; top: 92px;
    width: 230px;
    display: flex; flex-direction: column; align-items: center; gap: 18px;
  }
  .brand .dot {
    width: 84px; height: 84px; border-radius: 50%;
    background: var(--blue);
  }
  .brand .name {
    font-size: 28px; font-weight: 600; letter-spacing: 2px;
    color: var(--blue);
  }
  .divider {
    position: absolute;
    left: 300px; top: 84px;
    width: 2px; height: 176px;
    background: var(--blue);
  }
  .contact {
    position: absolute;
    left: 332px; top: 84px;
  }
  .contact .person {
    font-size: 23px; font-weight: 500; letter-spacing: 1.5px;
    color: var(--blue); text-transform: uppercase; line-height: 1.1;
  }
  .contact .role { font-size: 15px; margin-bottom: 14px; }
  .contact .address { font-size: 15px; line-height: 1.45; font-style: normal; margin-bottom: 10px; }
  .contact ul { list-style: none; }
  .contact li {
    font-size: 15px; line-height: 1.55;
    display: flex; align-items: center; gap: 8px;
  }
  .contact li svg { width: 11px; height: 11px; flex: none; }
  .contact .accent { color: var(--blue); }
</style>
</head>
<body>
  <section class="card card--front" aria-label="Card front">
    <div class="front-mark">
      <span class="dot"></span>
      <span class="name">VALTO Sàrl</span>
    </div>
  </section>

  <section class="card card--back" aria-label="Card back">
    <div class="brand">
      <span class="dot"></span>
      <span class="name">VALTO Sàrl</span>
    </div>
    <div class="divider"></div>
    <div class="contact">
      <p class="person">Elias Morand</p>
      <p class="role">President</p>
      <address class="address">Chemin des Prés 9<br>1027 Lonay</address>
      <ul>
        <li>
          <svg viewBox="0 0 12 12" aria-hidden="true"><path d="M3 1 L5 3 L4 4.5 Q5 7 7.5 8 L9 7 L11 9 L9.5 11 Q2 9 1 2.5 Z" fill="var(--blue)"/></svg>
          021 555 04 27
        </li>
        <li>
          <svg viewBox="0 0 12 12" aria-hidden="true"><rect x="1" y="2.5" width="10" height="7" fill="none" stroke="var(--blue)" stroke-width="1.2"/><path d="M1 2.5 L6 6.5 L11 2.5" fill="none" stroke="var(--blue)" stroke-width="1.2"/></svg>
          info@valto.ch
        </li>
        <li>
          <svg viewBox="0 0 12 12" aria-hidden="true"><circle cx="6" cy="6" r="5" fill="none" stroke="var(--blue)" stroke-width="1.1"/><ellipse cx="6" cy="6" rx="2.2" ry="5" fill="none" stroke="var(--blue)" stroke-width="1"/><path d="M1 6 H11" stroke="var(--blue)" stroke-width="1"/></svg>
          <span>www.<span class="accent">valto</span>.ch</span>
        </li>
      </ul>
    </div>
  </section>
</body>
</html>
```